Company Postage Label

Design a postage label that measures: 16cm long x 9cm high with a sticky back to stick on boxes. Similar to the attached from Talvora Carriers.

Industry/Entity Type

Motorcycle Part

Colors

Designer to choose colors to be used in the design.

Requirements
Must have
• Company logo and address

```html
<!DOCTYPE html>
<html lang="en">
<head>
<meta charset="utf-8">
<title>Rivetline Exhaust Co. — Postage Label</title>
<link href="https://fonts.googleapis.com/css2?family=Source+Sans+3:wght@400;600&display=swap" rel="stylesheet">
<style>
  :root {
    --page: #ffffff;
    --frame: #231f20;
    --panel: #ffffff;
    --ink: #1a1a1a;
    --rule: #2a2a2a;
    --badge: #050505;
    --badge-text: #ffffff;
  }
  html, body {
    margin: 0;
    padding: 0;
    width: 1200px;
    height: 1000px;
    overflow: hidden;
    background: var(--page);
  }
  .label {
    position: absolute;
    left: 162px;
    top: 252px;
    width: 875px;
    height: 493px;
    background: var(--frame);
    font-family: "Source Sans 3", "Myriad Pro", Arial, sans-serif;
    color: var(--ink);
  }
  .sender-panel {
    position: absolute;
    left: 33px;
    top: 33px;
    width: 231px;
    height: 427px;
    background: var(--panel);
  }
  .sender-panel svg { position: absolute; left: 0; top: 0; }
  .sender-heading {
    position: absolute;
    left: 33px;
    top: 387px;
    font-size: 16px;
    line-height: 1;
    transform-origin: left top;
    transform: rotate(-90deg);
    white-space: nowrap;
  }
  .recipient-panel {
    position: absolute;
    left: 280px;
    top: 33px;
    width: 562px;
    height: 427px;
    background: var(--panel);
  }
  .recipient-panel svg { position: absolute; left: 0; top: 0; }
  .brand-badge {
    position: absolute;
    left: 1px;
    top: 0;
    width: 172px;
    height: 124px;
    background: var(--badge);
    display: flex;
    align-items: center;
    justify-content: center;
  }
  .brand-name {
    color: var(--badge-text);
    font-weight: 600;
    font-size: 17px;
    letter-spacing: 0.5px;
    text-align: center;
    line-height: 1.15;
  }
  .stamp-note {
    position: absolute;
    left: 407px;
    top: 6px;
    font-size: 16px;
    line-height: 21px;
    margin: 0;
  }
  .recipient-heading {
    position: absolute;
    left: 24px;
    top: 171px;
    font-size: 16px;
    line-height: 1;
    margin: 0;
  }
</style>
</head>
<body>
  <div class="label">
    <section class="sender-panel">
      <svg width="231" height="427" aria-hidden="true">
        <g stroke="var(--rule)" stroke-width="2">
          <line x1="25" y1="37" x2="25" y2="389"/>
          <line x1="60" y1="37" x2="60" y2="389"/>
          <line x1="95" y1="37" x2="95" y2="389"/>
          <line x1="129" y1="37" x2="129" y2="389"/>
          <line x1="164" y1="37" x2="164" y2="389"/>
          <line x1="199" y1="37" x2="199" y2="389"/>
        </g>
      </svg>
      <span class="sender-heading">From</span>
    </section>

    <section class="recipient-panel">
      <div class="brand-badge">
        <span class="brand-name">RIVETLINE<br>EXHAUST CO.</span>
      </div>
      <p class="stamp-note">Please affix stamps<br>before mailing</p>
      <svg width="562" height="427" aria-hidden="true">
        <g stroke="var(--rule)" stroke-width="2" fill="none">
          <line x1="21" y1="170" x2="535" y2="170"/>
          <line x1="21" y1="204" x2="535" y2="204"/>
          <line x1="21" y1="239" x2="535" y2="239"/>
          <line x1="21" y1="273" x2="535" y2="273"/>
          <line x1="21" y1="308" x2="536" y2="308"/>
          <line x1="21" y1="343" x2="536" y2="343"/>
          <line x1="392" y1="308" x2="392" y2="343"/>
          <line x1="428" y1="308" x2="428" y2="343"/>
          <line x1="464" y1="308" x2="464" y2="343"/>
          <line x1="500" y1="308" x2="500" y2="343"/>
          <line x1="536" y1="308" x2="536" y2="343"/>
        </g>
      </svg>
      <p class="recipient-heading">To</p>
    </section>
  </div>
</body>
</html>
```